IT services company needs a business card designed

-2 sided business card.-Front is going to be the logo raised (3D floating effect) on a black background. Make the logos spider web shiny silver and keep the spider the same design. -Back needs to have the following information:Darrel Sotho, Managing Partner, Cell: 738-402-1954, Website: Plankhorn.com, Email: Darrel@Plankhorn.com
Target Market(s)
IT Services
Industry/Entity Type
It Company
Contact Information for Business Card
-2 sided business card.
-Front is going to be the logo raised (3D floating effect) on a black background. Make the logos spider web shiny silver and keep the spider the same design.
-Back needs to have the following information:
Darrel Sotho, Managing Partner, Cell: 738-402-1954, Website: Plankhorn.com, Email: Darrel@Plankhorn.com

```html
<!DOCTYPE html>
<html lang="en">
<head>
<meta charset="utf-8">
<title>Plankhorn Business Card</title>
<link href="https://fonts.googleapis.com/css2?family=Quicksand:wght@500;600;700&display=swap" rel="stylesheet">
<style>
  :root {
    --backdrop: #d4d4d4;
    --card-dark: #121212;
    --card-light: #ffffff;
    --accent: #1aa6e4;
    --accent-deep: #1680c4;
    --silver: #9a9a9a;
    --ink: #1e1e1e;
    --ink-soft: #3a3a3a;
  }
  * { margin: 0; padding: 0; box-sizing: border-box; }
  html, body { width: 1200px; height: 900px; overflow: hidden; }
  body {
    background: var(--backdrop);
    font-family: "Quicksand", sans-serif;
    position: relative;
  }
  .card {
    position: absolute;
    top: 313px;
    width: 475px;
    height: 263px;
    overflow: hidden;
  }
  .card-front { left: 43px; background: var(--card-dark); }
  .card-back { left: 627px; background: var(--card-light); }

  .front-wordmark {
    position: absolute;
    left: 0;
    width: 342px;
    top: 100px;
    text-align: center;
    color: #ffffff;
    font-weight: 600;
    font-size: 32px;
    letter-spacing: 1px;
  }
  .front-web-art {
    position: absolute;
    right: 0;
    top: 0;
    width: 125px;
    height: 263px;
    background: linear-gradient(180deg, rgba(26,166,228,0.55) 0%, rgba(26,166,228,0.35) 50%, rgba(154,154,154,0.35) 100%);
    border-radius: 80px 0 0 60px;
  }
  .back-web-art {
    position: absolute;
    left: 0;
    top: 0;
    width: 118px;
    height: 263px;
    background: linear-gradient(180deg, rgba(26,166,228,0.45) 0%, rgba(26,166,228,0.3) 55%, rgba(154,154,154,0.35) 100%);
    border-radius: 0 70px 50px 0;
  }
  .back-wordmark {
    position: absolute;
    right: 25px;
    top: 84px;
    color: var(--ink);
    font-weight: 600;
    font-size: 16px;
    letter-spacing: 0.5px;
  }
  .person {
    position: absolute;
    right: 25px;
    top: 128px;
    text-align: right;
  }
  .person-name {
    color: var(--accent-deep);
    font-weight: 700;
    font-size: 18px;
    line-height: 22px;
  }
  .person-title {
    color: var(--ink-soft);
    font-weight: 500;
    font-size: 14px;
    line-height: 18px;
  }
  .contact-list {
    position: absolute;
    right: 25px;
    top: 194px;
    list-style: none;
  }
  .contact-item {
    display: flex;
    justify-content: flex-end;
    align-items: center;
    height: 17.5px;
    color: var(--ink);
    font-weight: 500;
    font-size: 13.5px;
  }
  .contact-icon {
    width: 10px;
    height: 10px;
    margin-left: 14px;
    fill: var(--accent-deep);
  }
</style>
</head>
<body>
  <section class="card card-front">
    <div class="front-wordmark">PLANKHORN</div>
    <div class="front-web-art" role="img" aria-label="Spider on a silver and blue web illustration"></div>
  </section>

  <section class="card card-back">
    <div class="back-web-art" role="img" aria-label="Spider on a blue and grey web illustration"></div>
    <div class="back-wordmark">PLANKHORN</div>
    <div class="person">
      <div class="person-name">DARREL SOTHO</div>
      <div class="person-title">Managing Partner</div>
    </div>
    <ul class="contact-list">
      <li class="contact-item">738-402-1954
        <svg class="contact-icon" viewBox="0 0 10 10" aria-hidden="true"><path d="M1 4 Q5 0 9 4 L8 5 L6.5 4 L6.5 3.2 Q5 2.6 3.5 3.2 L3.5 4 L2 5 Z M2.5 6 h5 v3 h-5 Z"/></svg>
      </li>
      <li class="contact-item">Plankhorn.com
        <svg class="contact-icon" viewBox="0 0 10 10" aria-hidden="true"><path d="M0.5 5 L9.5 1 L7 9.5 L5 6.5 Z"/></svg>
      </li>
      <li class="contact-item">Darrel@Plankhorn.com
        <svg class="contact-icon" viewBox="0 0 10 10" aria-hidden="true"><circle cx="5" cy="5" r="4.5"/><path d="M0.5 5 h9 M5 0.5 v9 M5 0.5 Q2 5 5 9.5 M5 0.5 Q8 5 5 9.5" stroke="#fff" stroke-width="0.7" fill="none"/></svg>
      </li>
    </ul>
  </section>
</body>
</html>
```